hfdhddfgfhfghfghgfhfhfhgfhfhfh

Industry/Entity Type

Painting

Logo Text

TOLVEN Painting

Logo styles of interest
Wordmark Logo
Requirements
Should not have
• Paintbrushes or rollers etc....

```html
<!DOCTYPE html>
<html lang="en">
<head>
<meta charset="utf-8">
<title>Tolven Painting – Business Card</title>
<link rel="stylesheet" href="https://fonts.googleapis.com/css2?family=Fauna+One&display=swap">
<style>
  :root {
    --backdrop: #3b3b3d;
    --card-white: #ffffff;
    --paint-blue: #2f87c9;
    --ink: #141414;
    --label-white: #ffffff;
    --font-main: "Fauna One", Georgia, serif;
  }
  * { box-sizing: border-box; margin: 0; padding: 0; }
  html, body {
    width: 1200px;
    height: 1000px;
    overflow: hidden;
    background: var(--backdrop);
    font-family: var(--font-main);
  }
  .canvas {
    position: relative;
    width: 1200px;
    height: 1000px;
  }
  .card {
    position: absolute;
    width: 600px;
    height: 350px;
    overflow: hidden;
    box-shadow: 0 10px 24px rgba(0, 0, 0, 0.45);
  }

  /* Front */
  .card-front {
    left: 70px;
    top: 100px;
    background: var(--card-white);
  }
  .splash-area {
    position: absolute;
    left: 0;
    bottom: 0;
    width: 340px;
    height: 300px;
    background: radial-gradient(ellipse at 15% 90%, var(--paint-blue) 0%, rgba(47, 135, 201, 0.75) 35%, rgba(47, 135, 201, 0) 72%);
  }
  .wordmark {
    position: absolute;
    right: 38px;
    top: 42px;
    font-size: 50px;
    color: var(--ink);
    letter-spacing: 0.5px;
    white-space: nowrap;
  }
  .person {
    position: absolute;
    right: 40px;
    top: 128px;
    text-align: right;
  }
  .person-name {
    font-size: 25px;
    color: var(--paint-blue);
  }
  .person-role {
    font-size: 17px;
    color: var(--ink);
    margin-top: 2px;
  }
  .contact {
    position: absolute;
    right: 40px;
    top: 222px;
    display: grid;
    grid-template-columns: auto auto;
    column-gap: 14px;
    row-gap: 1px;
    font-size: 14px;
    color: var(--ink);
    text-align: right;
  }
  .contact .kind { text-align: left; }

  /* Back */
  .card-back {
    left: 540px;
    top: 500px;
    background: var(--paint-blue);
  }
  .splash-texture {
    position: absolute;
    inset: 0;
    background:
      radial-gradient(ellipse at 12% 85%, rgba(255, 255, 255, 0.35) 0%, rgba(255, 255, 255, 0) 30%),
      radial-gradient(ellipse at 80% 20%, rgba(255, 255, 255, 0.3) 0%, rgba(255, 255, 255, 0) 28%),
      radial-gradient(ellipse at 90% 90%, rgba(255, 255, 255, 0.25) 0%, rgba(255, 255, 255, 0) 22%);
  }
  .services {
    position: absolute;
    left: 0;
    right: 0;
    top: 150px;
    text-align: center;
    font-size: 30px;
    color: var(--label-white);
    white-space: nowrap;
  }

  .side-label {
    position: absolute;
    font-size: 34px;
    color: var(--label-white);
  }
  .label-front { left: 90px; top: 540px; }
  .label-back { left: 860px; top: 880px; }
</style>
</head>
<body>
  <main class="canvas">
    <section class="card card-front" aria-label="Business card front">
      <div class="splash-area" role="img" aria-label="Blue paint splash decoration"></div>
      <h1 class="wordmark">Tolven Painting</h1>
      <div class="person">
        <p class="person-name">Marten Tolven</p>
        <p class="person-role">Managing Director</p>
      </div>
      <div class="contact">
        <span>0438516290</span><span class="kind">(mobile)</span>
        <span>tolvenpainting@mail.com</span><span class="kind">(email)</span>
        <span>31 567 902 118</span><span class="kind">(ABN)</span>
      </div>
    </section>
    <p class="side-label label-front">front</p>

    <section class="card card-back" aria-label="Business card back">
      <div class="splash-texture" role="img" aria-label="White paint splatter texture on blue"></div>
      <p class="services">Domestic . Residential . Commercial</p>
    </section>
    <p class="side-label label-back">back</p>
  </main>
</body>
</html>
```